Business Card for Maplethorne Elder Keepers

I need a business card design for a very elite and personalized companion care company. We take care of the client at home with respect, dignity, and our full attention. The design should communicate a classic elegance and trust.

/Users/lorafenwick/Downloads/graphwellhub_121488_23943024_3826329_sourcefile

```html
<!DOCTYPE html>
<html lang="en">
<head>
<meta charset="utf-8">
<title>Maplethorne Elder Keepers – Business Card</title>
<link rel="stylesheet" href="https://fonts.googleapis.com/css2?family=Cinzel:wght@400&family=Arimo:wght@400&display=swap">
<style>
  :root {
    --backdrop: #a3a3a3;
    --navy: #05477a;
    --sky: #2aa9e3;
    --sky-bright: #00b8f1;
    --white: #ffffff;
    --grad-dark: #065a98;
    --grad-light: #02c0fb;
  }
  * { margin: 0; padding: 0; box-sizing: border-box; }
  html, body { width: 1200px; height: 802px; overflow: hidden; }
  body { background: var(--backdrop); position: relative; font-family: "Arimo", Arial, sans-serif; }

  .card {
    position: absolute;
    top: 274px;
    width: 443px;
    height: 265px;
    overflow: hidden;
    box-shadow: 0 3px 6px rgba(0,0,0,0.35);
  }
  .card--front { left: 136px; background: var(--white); }
  .card--back {
    left: 624px;
    background: linear-gradient(30deg, var(--grad-dark) 0%, #0590cf 55%, var(--grad-light) 100%);
  }

  .front-shape { position: absolute; inset: 0; width: 100%; height: 100%; }

  .holder-name {
    position: absolute; left: 24px; top: 33px;
    font-family: "Cinzel", Georgia, serif;
    font-size: 17px; color: var(--sky); letter-spacing: 0.2px;
  }
  .holder-role {
    position: absolute; left: 24px; top: 55px;
    font-size: 13px; color: var(--white);
  }
  .contact-list {
    position: absolute; left: 24px; top: 86px;
    list-style: none; color: var(--white); font-size: 13px; line-height: 16.5px;
  }
  .contact-list li { display: flex; align-items: center; gap: 4px; }
  .contact-list svg { width: 11px; height: 11px; flex: none; }
  .address {
    position: absolute; left: 24px; top: 156px;
    color: var(--white); font-size: 13px; line-height: 16.5px; font-style: normal;
  }

  .brand-name {
    position: absolute;
    font-family: "Cinzel", Georgia, serif;
    text-align: center; line-height: 1.1;
  }
  .brand-name .line-main { display: block; }
  .brand-name .line-sub { display: block; }
  .card--front .brand-name {
    right: 20px; top: 184px; color: var(--navy);
  }
  .card--front .line-main { font-size: 22px; }
  .card--front .line-sub { font-size: 13px; letter-spacing: 1px; }
  .card--back .brand-name {
    left: 0; right: 0; top: 108px; color: var(--white);
  }
  .card--back .line-main { font-size: 30px; }
  .card--back .line-sub { font-size: 16px; letter-spacing: 1.5px; }
</style>
</head>
<body>
  <section class="card card--front" aria-label="Business card front">
    <svg class="front-shape" viewBox="0 0 545 326" preserveAspectRatio="none" aria-hidden="true">
      <path d="M0,0 H375 C425,0 432,55 418,100 C395,170 320,215 215,250 C150,272 112,292 110,326 H0 Z" fill="var(--navy)"/>
      <path d="M375,0 C425,0 432,55 418,100 C395,170 320,215 215,250 C150,272 112,292 110,326" fill="none" stroke="var(--sky-bright)" stroke-width="4"/>
    </svg>
    <h1 class="holder-name">EDMUND HARROW</h1>
    <p class="holder-role">Managing Director</p>
    <ul class="contact-list">
      <li><svg viewBox="0 0 12 12"><path d="M1,4 C1,2 3,1 6,1 C9,1 11,2 11,4 L9,5 L8,3.5 H4 L3,5 Z M3,6 H9 L10,11 H2 Z" fill="var(--sky)"/></svg>044-987 654 321</li>
      <li><svg viewBox="0 0 12 12"><rect x="1" y="2.5" width="10" height="7" fill="var(--sky)"/><path d="M1,2.5 L6,7 L11,2.5" fill="none" stroke="var(--navy)" stroke-width="1"/></svg>hello@eldermail.com</li>
      <li><svg viewBox="0 0 12 12"><circle cx="6" cy="6" r="5" fill="var(--sky)"/><path d="M4,3 C5,4 6,4 5,6 C4,7 6,8 7,10 M8,2.5 C7,4 9,5 10,5" fill="none" stroke="var(--navy)" stroke-width="1"/></svg>www.homecaresite.com</li>
    </ul>
    <address class="address">421, Address line here<br>Country Name, 45452</address>
    <div class="brand-name">
      <span class="line-main">MAPLETHORNE</span>
      <span class="line-sub">ELDER KEEPERS</span>
    </div>
  </section>

  <section class="card card--back" aria-label="Business card back">
    <div class="brand-name">
      <span class="line-main">MAPLETHORNE</span>
      <span class="line-sub">ELDER KEEPERS</span>
    </div>
  </section>
</body>
</html>
```